Training company needs a Quick Reference Card design

We have draft skeleton of the design and most of the text. But we need a designer to take it the rest if the way.
I have designed a 2 page quick reference card - it is meant to be a 2-sided document. The first page is portrait, the back page can either be portrait or landscape, I'm not too concerned, whichever fits best.
Section called 'Maps' on front, a map is a collection of documents (like a manual), a topic is a document (like a page or section of a manual) and a block is a section of a document. The graphic is mean to illustrate the hierarchy but essentially a map is a big document with smaller documents in it.
Please use the company's logo colors to differentiate the different sections with minimal/ highlight only use of the darkest color, preferably.
Please use the icons for the corresponding Information types in the chart of the back - except please re-design the icons color scheme to match the company's logo/website colors.

Target Market(s)

Technical writers, after attending our training course, as an ongoing resource for them

Industry/Entity Type

It Company

Font styles to use
Sans Serif

Requirements
Must have
• Must adhere to look and feel of brand/ website. www.lumenrivet.com
Nice to have
• Please keep the design modern and slick looking, not too busy, easy to read

```html
<!DOCTYPE html>
<html lang="en">
<head>
<meta charset="utf-8">
<title>Quick Reference Card</title>
<link href="https://fonts.googleapis.com/css2?family=Roboto:wght@400;500;700&display=swap" rel="stylesheet">
<style>
  :root {
    --navy: #201c85;
    --cyan: #27c3f3;
    --ink: #1c1c3a;
    --white: #ffffff;
  }
  * { margin: 0; padding: 0; box-sizing: border-box; }
  html, body { width: 887px; height: 1200px; overflow: hidden; background: var(--white); }
  body { font-family: "Roboto", Arial, sans-serif; color: var(--ink); }
  .card { position: relative; width: 887px; height: 1200px; background: var(--white); }
  .abs { position: absolute; }

  /* header */
  .brand { left: 26px; top: 14px; height: 96px; display: flex; align-items: center; gap: 14px; }
  .brand-dot { width: 78px; height: 78px; border-radius: 50%; background: var(--navy); }
  .brand-name { font-size: 30px; font-weight: 700; color: var(--navy); letter-spacing: 0.5px; line-height: 1; }
  .title { left: 372px; top: 40px; width: 500px; text-align: right; font-size: 37px; font-weight: 500;
           color: var(--navy); letter-spacing: 1.5px; }

  /* map and definitions */
  .map-panel { left: 0; top: 121px; width: 406px; height: 290px; background: var(--navy);
               border-radius: 0 8px 8px 0; color: var(--white); text-align: center; }
  .map-title { position: absolute; left: 0; right: 0; top: 14px; font-size: 27px; font-weight: 500; }
  .map-col { position: absolute; top: 58px; width: 170px; }
  .map-col.left { left: 40px; }
  .map-col.right { left: 224px; }
  .map-topic { font-size: 24px; font-weight: 500; }
  .map-block { font-size: 17px; font-weight: 700; line-height: 1.35; margin-top: 22px; }
  .map-sub { margin-top: 32px; }

  .definitions { left: 424px; top: 121px; width: 463px; height: 290px; background: var(--cyan);
                 border-radius: 8px 0 0 8px; color: var(--white); padding: 18px 24px 0 30px;
                 font-size: 17.5px; line-height: 1.38; }
  .definitions p + p { margin-top: 19px; }
  .definitions strong { font-weight: 700; }

  /* section bands */
  .band { left: 0; width: 887px; background: var(--navy); color: var(--white); text-align: center;
          font-size: 26px; font-weight: 700; letter-spacing: 0.5px; }
  .rules-band { top: 421px; height: 50px; line-height: 50px; }

  /* writing rules */
  .rule { top: 478px; width: 280px; }
  .rule-head { display: flex; align-items: center; gap: 10px; height: 70px; }
  .rule-icon { width: 66px; height: 66px; flex: none; }
  .rule-title { flex: 1; text-align: center; color: var(--cyan); font-size: 25px; font-weight: 500;
                line-height: 1.1; letter-spacing: 0.5px; }
  .rule-text { margin-top: 8px; text-align: center; font-size: 16.5px; line-height: 1.38; }
  .rule.sentences { left: 26px; }
  .rule.characters { left: 294px; }
  .rule.language { left: 594px; }

  /* questions and language arts */
  .questions { left: 0; top: 683px; width: 500px; height: 236px; background: var(--navy);
               border-radius: 0 8px 8px 0; color: var(--white); }
  .questions h2 { text-align: center; color: var(--cyan); font-size: 24px; font-weight: 500;
                  line-height: 1.15; margin-top: 22px; letter-spacing: 0.5px; }
  .questions ol { margin: 16px 0 0 58px; font-size: 20px; line-height: 1.3; padding-left: 22px; }
  .questions li { padding-left: 14px; margin-bottom: 6px; }

  .arts { left: 513px; top: 683px; width: 374px; height: 236px; background: var(--navy);
          border-radius: 8px 0 0 8px; color: var(--white); }
  .arts h2 { text-align: center; color: var(--cyan); font-size: 24px; font-weight: 500;
             line-height: 1.15; margin-top: 22px; letter-spacing: 0.5px; }
  .arts dl { margin: 28px 0 0 12px; font-size: 19.5px; line-height: 1.25; }
  .arts dd { margin-bottom: 6px; }
  .arts dt { display: inline; font-weight: 500; }

  /* cognitive principles */
  .principles { left: 0; top: 931px; width: 887px; height: 269px; background: var(--navy); color: var(--white); }
  .principles h2 { text-align: center; font-size: 27px; font-weight: 700; margin-top: 14px; letter-spacing: 0.5px; }
  .principle-grid { display: grid; grid-template-columns: 232px 210px 212px 222px; margin: 12px 0 0 4px; }
  .principle h3 { color: var(--cyan); font-size: 22px; font-weight: 500; text-align: center; letter-spacing: 0.5px; }
  .principle p { margin-top: 8px; text-align: center; font-size: 15.5px; line-height: 1.4; padding: 0 12px; }
</style>
</head>
<body>
<main class="card">
  <header>
    <div class="abs brand">
      <span class="brand-dot"></span>
      <span class="brand-name">LUMENRIVET.com</span>
    </div>
    <h1 class="abs title">QUICK REFERENCE CARD</h1>
  </header>

  <section class="abs map-panel" aria-label="Map hierarchy">
    <div class="map-title">MAP</div>
    <div class="map-col left">
      <div class="map-topic">TOPIC</div>
      <div class="map-block">PRIMARY<br>BLOCK</div>
      <div class="map-block map-sub">SUB<br>BLOCK</div>
    </div>
    <div class="map-col right">
      <div class="map-topic">TOPIC</div>
      <div class="map-block">PRIMARY<br>BLOCK</div>
      <div class="map-block map-sub">SUB<br>BLOCK</div>
    </div>
  </section>

  <section class="abs definitions">
    <p><strong>A map</strong> is a file that organizes topics into structured collections of information. Maps specify hierarchy and relationships among topics.</p>
    <p><strong>A topic</strong> is a group of related blocks with a title. Use the chunking principle to group together relevant blocks.</p>
    <p><strong>A block</strong> is a bite-sized chunk of information about one main idea that allows the writer to organize the material into logical sections.</p>
  </section>

  <h2 class="abs band rules-band">GENERAL WRITING RULES</h2>

  <section class="abs rule sentences">
    <div class="rule-head">
      <svg class="rule-icon" viewBox="0 0 66 66" aria-hidden="true"><circle cx="33" cy="33" r="33" fill="#27c3f3"/><polyline points="18,34 29,45 49,22" fill="none" stroke="#fff" stroke-width="7" stroke-linecap="round" stroke-linejoin="round"/></svg>
      <h3 class="rule-title">EFFECTIVE<br>SENTENCES</h3>
    </div>
    <p class="rule-text">One main agent, action &amp; outcome. Use active voice and simplest tense possible. No more than 7 sentences per paragraph. Use lists and tables.</p>
  </section>

  <section class="abs rule characters">
    <div class="rule-head">
      <svg class="rule-icon" viewBox="0 0 66 66" aria-hidden="true"><circle cx="33" cy="33" r="33" fill="#27c3f3"/><polyline points="18,34 29,45 49,22" fill="none" stroke="#fff" stroke-width="7" stroke-linecap="round" stroke-linejoin="round"/></svg>
      <h3 class="rule-title">SPECIAL<br>CHARACTERS</h3>
    </div>
    <p class="rule-text">Avoid special characters, spell out words instead. Remove parentheses, colons and dashes. Avoid using quotation marks and slashes.</p>
  </section>

  <section class="abs rule language">
    <div class="rule-head">
      <svg class="rule-icon" viewBox="0 0 66 66" aria-hidden="true"><circle cx="33" cy="33" r="33" fill="#27c3f3"/><polyline points="18,34 29,45 49,22" fill="none" stroke="#fff" stroke-width="7" stroke-linecap="round" stroke-linejoin="round"/></svg>
      <h3 class="rule-title">PLAIN<br>LANGUAGE</h3>
    </div>
    <p class="rule-text">Write in short sentences. Provide useful titles. Use clear familiar words. Avoid excess words.<br>Be consistent.</p>
  </section>

  <section class="abs questions">
    <h2>3 QUESTIONS TO ASK BEFORE<br>YOU START WRITING</h2>
    <ol>
      <li>What is the purpose of this information?</li>
      <li>What is the desired user response of this information?</li>
      <li>Who is the audience?</li>
    </ol>
  </section>

  <section class="abs arts">
    <h2>2 TYPES OF<br>LANGUAGE ARTS:</h2>
    <dl>
      <dd><dt>LAFI</dt> Language arts for information</dd>
      <dd><dt>LAFPR</dt><br>language arts for personal response</dd>
    </dl>
  </section>

  <section class="abs principles">
    <h2>4 COGNITIVE PRINCIPLES</h2>
    <div class="principle-grid">
      <div class="principle">
        <h3>CONSISTENCY</h3>
        <p>Use similar terms and structures.Pick a term and stick with it. Use the same sequence of blocks. Use consistent styles.</p>
      </div>
      <div class="principle">
        <h3>CHUNKING</h3>
        <p>Maximum of nine (7 +/- 2) items in a list, rows in a table, blocks in a topic, ortopics in a map.</p>
      </div>
      <div class="principle">
        <h3>RELEVANCE</h3>
        <p>Group similar items together. Separate relevance? Separate block. Irrelevant? Delete it.</p>
      </div>
      <div class="principle">
        <h3>TITLING</h3>
        <p>Name everything. Name every block, every topic, every map and every table column.</p>
      </div>
    </div>
  </section>
</main>
</body>
</html>
```